Letterhead design for Dental Practice - Ashby Lane Dental Care

Letterhead for Private Dental Practice. To be used for all official correspondance and for printing treatment details on to be given to patients.

Target Market(s)

Private dental patients

Industry/Entity Type

Dental Clinic

Font styles to use
Other font styles liked:
• nexa-light

Colors
33a6d7
1c66ac
85abd2

Requirements
Must have
• info in the footer and header needs to be 3.5cm from upper/lower boader of paper, see photo in uploaded files
• info details:
• tel. 0115 947 3208
• email info@ashbylanedc.co.uk
• ashbylanedentalcare.co.uk
• 17b Ashby Lane West Bridgford Nottingham NG2 7QT
• nexa-light font as in uploaded logo files
Should not have
• No funny tooth pictures

```html
<!DOCTYPE html>
<html lang="en">
<head>
<meta charset="utf-8">
<title>Ashby Lane Dental Care – Letterhead</title>
<link href="https://fonts.googleapis.com/css2?family=Montserrat:wght@300;400&family=Open+Sans:wght@400;600&display=swap" rel="stylesheet">
<style>
  :root {
    --brand-blue: #1f9fdc;
    --brand-navy: #1c66ac;
    --accent-dark: #4a4a4a;
    --text: #3d3d3d;
    --rule: #9a9a9a;
    --paper: #ffffff;
    --backdrop: #e9e9e9;
    --signature-tone: #e4e4e4;
  }
  * { margin: 0; padding: 0; box-sizing: border-box; }
  html, body { width: 1040px; height: 1200px; overflow: hidden; background: var(--backdrop); }
  .letterhead {
    position: absolute; left: 53px; top: 0; width: 933px; height: 1200px;
    background: var(--paper); color: var(--text);
    font-family: "Open Sans", Arial, sans-serif;
  }
  .side-band { position: absolute; left: 0; top: 0; width: 24px; height: 100%; background: var(--brand-blue); }
  .side-band__pattern { position: absolute; left: 0; width: 24px; background: var(--accent-dark); }
  .side-band__pattern--upper { top: 141px; height: 87px; }
  .side-band__pattern--lower { top: 339px; height: 77px; }

  .brand { position: absolute; right: 42px; top: 118px; display: flex; align-items: center; gap: 12px; }
  .brand__dot { width: 22px; height: 22px; border-radius: 50%; background: var(--brand-blue); }
  .brand__name { font-family: "Montserrat", Arial, sans-serif; font-weight: 300; font-size: 30px; color: var(--brand-blue); letter-spacing: 0.2px; white-space: nowrap; }

  .letter { position: absolute; left: 87px; width: 754px; font-size: 14.5px; line-height: 18px; }
  .letter p { margin: 0; }
  .issue-date { top: 217px; }
  .recipient { top: 253px; }
  .salutation { top: 357px; }
  .body-text { top: 407px; line-height: 27px; text-align: justify; hyphens: auto; }
  .body-text p + p { margin-top: 27px; }
  .closing { top: 816px; }
  .signature { position: absolute; left: 87px; top: 850px; width: 215px; height: 30px; background: linear-gradient(90deg, var(--signature-tone), #f3f3f3); border-radius: 3px; }
  .signatory { position: absolute; left: 87px; top: 892px; font-size: 19px; font-weight: 600; color: #333; }
  .signatory-role { position: absolute; left: 87px; top: 924px; font-size: 14.5px; }

  .contact-row { position: absolute; top: 1096px; left: 0; width: 100%; font-family: "Montserrat", Arial, sans-serif; font-weight: 300; font-size: 14px; color: #333; }
  .contact { position: absolute; display: flex; align-items: center; gap: 9px; white-space: nowrap; }
  .contact--phone { left: 147px; }
  .contact--email { left: 338px; }
  .contact--web { left: 625px; }
  .contact svg { width: 24px; height: 24px; display: block; }
  .footer-rule { position: absolute; left: 83px; width: 757px; top: 1138px; height: 1px; background: var(--rule); }
  .footer-address { position: absolute; left: 0; width: 100%; top: 1158px; text-align: center; font-family: "Montserrat", Arial, sans-serif; font-weight: 300; font-size: 14px; color: #333; }
</style>
</head>
<body>
<main class="letterhead" lang="en">
  <div class="side-band">
    <div class="side-band__pattern side-band__pattern--upper" role="img" aria-label="Stacked chevron ornament"></div>
    <div class="side-band__pattern side-band__pattern--lower" role="img" aria-label="Stacked chevron ornament"></div>
  </div>

  <header class="brand">
    <span class="brand__dot"></span>
    <span class="brand__name">Ashby Lane Dental Care</span>
  </header>

  <p class="letter issue-date">Issuing Date: May 5, 2018</p>
  <div class="letter recipient">
    <p>Name Of Employee Mr. XYZABC</p>
    <p>Address of Employee</p>
    <p>Address Line 2 etc..</p>
  </div>
  <p class="letter salutation">Dear Mr.XYZABC</p>

  <div class="letter body-text">
    <p>Lorem Ipsum has been the industry's standard dummy text ever since the 1500s, when an unknown printer took a galley of type and scrambled it to make a type specimen book. It has survived not only five centuries, but also the leap into electronic typesetting, remaining essentially unchanged. It was popularised in the 1960s with the release of Typeline sheets containing Lorem Ipsum passages, and more recently with desktop publishing software like Pagewright Studio including versions of Lorem Ipsum.</p>
    <p>Lorem Ipsum is simply dummy text of the printing and typesetting industry. Lorem Ipsum has been the industry's standard dummy text ever since the 1500s, when an unknown printer took a galley of type and scrambled it to make a type specimen book.</p>
    <p>It has survived not only five centuries, but also the leap into electronic typesetting, remaining essentially unchanged. It was popularised in the 1960s with the release of Typeline sheets containing Lorem IpsumIpsum passages.</p>
  </div>

  <p class="letter closing">Yours Sincerely</p>
  <div class="signature" role="img" aria-label="Handwritten signature"></div>
  <p class="signatory">Daniel Harwood</p>
  <p class="signatory-role">Managing Director</p>

  <footer>
    <div class="contact-row">
      <div class="contact contact--phone">
        <svg viewBox="0 0 24 24" aria-hidden="true"><circle cx="12" cy="12" r="12" fill="var(--brand-blue)"/><path d="M8.6 6.5l1.8-.3 1.1 2.8-1.3 1c.6 1.4 1.6 2.5 3 3.2l1.1-1.3 2.8 1.1-.3 1.8c-.2.7-.8 1.1-1.5 1-4.3-.5-7.5-3.7-8-8-.1-.6.4-1.2 1.3-1.3z" fill="#fff"/></svg>
        <span>0115 947 3208</span>
      </div>
      <div class="contact contact--email">
        <svg viewBox="0 0 24 24" aria-hidden="true"><circle cx="12" cy="12" r="12" fill="var(--brand-blue)"/><rect x="6.5" y="8" width="11" height="8" rx="1" fill="none" stroke="#fff" stroke-width="1.4"/><path d="M6.8 8.5L12 12.6l5.2-4.1" fill="none" stroke="#fff" stroke-width="1.4"/></svg>
        <span>info@ashbylanedc.co.uk</span>
      </div>
      <div class="contact contact--web">
        <svg viewBox="0 0 24 24" aria-hidden="true"><circle cx="12" cy="12" r="12" fill="var(--brand-blue)"/><circle cx="12" cy="12" r="6" fill="none" stroke="#fff" stroke-width="1.4"/><path d="M6 12h12M12 6c-2.2 2.8-2.2 9.2 0 12M12 6c2.2 2.8 2.2 9.2 0 12" fill="none" stroke="#fff" stroke-width="1.2"/></svg>
        <span>www.ashbylanedentalcare.co.uk</span>
      </div>
    </div>
    <div class="footer-rule"></div>
    <p class="footer-address">17b Ashby Lane West&nbsp; Fernbridge Holmsworth HW2 7QT</p>
  </footer>
</main>
</body>
</html>
```